Modern and sophisticated web design for architect/designer

Lumo Vant is a Building Design & Drafting studio based in Nedlands Western Australia, providing a high quality and complete client service from concept design through Council planning approvals and building licenses to construction drawings for kitchens and bathrooms, extensions, additions, renovations and new homes.

Lumo Vant is looking for a new qwerty design that *is different from a normal* 2/3 column website. The website design must be very arty, clean and catchy. This design needs to be very different and must not look like a downloadable template.

The design must be able to display a lot of photos for the different projects.

The design must comply with W3C standards (i.e. use of fonts) and must be delivered to us in A PSD layered format.

Here are a couple of example website designs that exemplify what I am after:
1) http://www.prtd.com.au/
2) http://www.martinholsbyarchitect.com/en/
3) http://veromiks.com/

I particularly like numbers 1 and 2. The third, Veromiks, jumps around a little between pages as it is actually several companies. I prefer the page design to remain steady if possible.

I like the very clever nature of number 1 (PRTD). It captures the interest, although slightly gimmicky, however I think it doesn't overpower. Its modern, and visual.

I like the clean elegant design of number 2 (Holsby), it simply delivers everything necessary in a clear intelligent manner, its attractive, menu is clever simple to use and attractive.

I would be very happy to have either of these websites.

here is another one:
4) http://www.tqarchitect.com.au/

Although this is similarly elegant, it appears quite dated. I don't like the thumbnails that you click on in the gallery, its quite clumsy. It looks minimalist, and IS minimalist, doesn't look like there is much option to expand other than changing the pictures.

If you look at my own website:
http://www.lumovant.com.au

I designed and built it myself without any skills or experience. I had to use a generic photo album generator which was worse than useless, the point I am trying to make is I tried to make the menu system a little unusual, I tried to keep the pages neat and tidy, and totally used the "black website" method. However I am more inclined to go with the lighter/white pages of (1) and (2) above because they tend to show photos better.

Dear Designers. 

ArtHive Administration has worked to provide a more comprehensive brief. Please review the amended description. 

Kind Regards, Wesley. 

Target Market(s)

Target market is people who are looking to renovate their home

Industry/Entity Type

Construction

Requirements
Must have
• The brief is to design a visual modern, elegant, sophisticated website for a small scale designer/photographer/architect that looks itself like it is designed. Not off the shelf, simple and dated. Basically the design itself has to exemplify me, it has to say "this guy is a designer, and he is good at it".

```html
<!DOCTYPE html>
<html lang="en">
<head>
<meta charset="utf-8">
<title>Lumo Vant — Building Design &amp; Drafting</title>
<link rel="stylesheet" href="https://fonts.googleapis.com/css2?family=Arimo:wght@400;700&display=swap">
<style>
  :root {
    --header-top: #22405c;
    --header-bottom: #04090c;
    --page-dark: #050d12;
    --page-mid: #0c1c27;
    --page-blue: #1d3a55;
    --footer-bg: #0b1a26;
    --accent: #7fbbe0;
    --nav-text: #e8eef2;
    --body-text: #e4e8ea;
    --footer-text: #7d9db5;
    --card-bg: #ffffff;
    --card-label: #3a3a3a;
    --dot: #c9c9c9;
  }
  * { box-sizing: border-box; margin: 0; padding: 0; }
  html, body { width: 1200px; height: 964px; overflow: hidden; }
  body {
    font-family: "Arimo", Arial, sans-serif;
    background: var(--page-dark);
    position: relative;
  }

  .site-header {
    position: absolute; left: 0; top: 0; width: 1200px; height: 151px;
    background: linear-gradient(180deg, var(--header-top) 0%, #132636 45%, var(--header-bottom) 100%);
  }
  .brand {
    position: absolute; left: 90px; top: 20px;
    font-size: 30px; font-weight: 700; letter-spacing: 6px;
    color: #f2f4f6; text-transform: uppercase;
    display: flex; align-items: center; gap: 12px;
  }
  .brand-mark { width: 14px; height: 14px; background: #f2f4f6; }
  .call-us {
    position: absolute; left: 703px; top: 28px;
    font-size: 17px; color: #ffffff;
  }
  .search {
    position: absolute; left: 918px; top: 21px; width: 192px; height: 32px;
    background: #ffffff; border: 1px solid #c8c8c8;
    display: flex; align-items: center; justify-content: space-between;
    padding: 0 8px 0 11px; font-size: 11px; color: #333;
  }
  .main-nav {
    position: absolute; right: 90px; top: 99px;
    display: flex; gap: 45px; list-style: none;
    font-size: 15px; text-transform: uppercase; color: var(--nav-text);
  }
  .main-nav .is-current { color: var(--accent); }

  .hero {
    position: absolute; left: 0; top: 151px; width: 1200px; height: 354px;
    background: linear-gradient(90deg, #2a1f12 0%, #0d0d0a 58%, #0b1114 100%);
  }
  .hero-photo {
    position: absolute; left: 0; top: 0; width: 730px; height: 354px;
    background:
      radial-gradient(ellipse at 45% 45%, rgba(214,150,70,0.75) 0%, rgba(120,80,35,0.5) 35%, rgba(20,25,18,0) 75%),
      linear-gradient(90deg, #1f2a18 0%, #3d3020 50%, #0d0f0c 100%);
  }
  .hero-copy {
    position: absolute; left: 689px; top: 100px; width: 421px;
  }
  .section-title {
    font-variant: small-caps; font-weight: 400; color: var(--accent);
    font-size: 26px; letter-spacing: 0.5px;
  }
  .hero-copy p {
    margin-top: 10px; font-size: 13.4px; line-height: 23px;
    color: var(--body-text); text-align: justify;
  }
  .slider-dots {
    position: absolute; left: 997px; top: 310px; display: flex; gap: 14px;
  }
  .slider-dots span { width: 18px; height: 18px; border-radius: 50%; background: var(--dot); }
  .slider-dots .is-active { background: #4a4a4a; border: 2px solid #d8d8d8; }

  .services {
    position: absolute; left: 0; top: 505px; width: 1200px; height: 356px;
    background: linear-gradient(180deg, var(--page-dark) 0%, var(--page-mid) 45%, var(--page-blue) 100%);
  }
  .services .section-title { position: absolute; left: 90px; top: 41px; font-size: 27px; }
  .carousel-arrows { position: absolute; left: 1076px; top: 52px; display: flex; gap: 10px; }
  .service-card {
    position: absolute; top: 83px; width: 324px; height: 231px;
    background: var(--card-bg); padding: 12px 12px 0;
    box-shadow: 0 0 10px rgba(0,0,0,0.35);
  }
  .service-photo { width: 300px; height: 163px; }
  .service-card h3 {
    text-align: center; font-weight: 400; font-size: 17.5px;
    color: var(--card-label); margin-top: 20px; text-transform: uppercase;
  }

  .site-footer {
    position: absolute; left: 0; top: 861px; width: 1200px; height: 103px;
    background: var(--footer-bg); color: var(--footer-text); font-size: 14px;
  }
  .footer-nav { position: absolute; left: 90px; top: 25px; display: flex; gap: 10px; list-style: none; }
  .copyright { position: absolute; left: 90px; top: 58px; word-spacing: 3px; }
  .social { position: absolute; left: 1056px; top: 38px; display: flex; gap: 6px; }
  .social span { width: 24px; height: 24px; border-radius: 3px; background: #3b5a98; }
  .social span + span { background: #4fb6e6; }
</style>
</head>
<body>
  <header class="site-header">
    <div class="brand"><span class="brand-mark"></span>Lumo Vant</div>
    <div class="call-us">CALL US : 555 014 2270</div>
    <div class="search">
      <span>Search</span>
      <svg width="16" height="16" viewBox="0 0 16 16" aria-hidden="true">
        <circle cx="6.5" cy="6.5" r="4.5" fill="#222"/>
        <line x1="9.5" y1="9.5" x2="14" y2="14" stroke="#222" stroke-width="3" stroke-linecap="round"/>
      </svg>
    </div>
    <ul class="main-nav">
      <li class="is-current">Home</li>
      <li>About</li>
      <li>Services</li>
      <li>Projects</li>
      <li>Contact</li>
    </ul>
  </header>

  <section class="hero">
    <div class="hero-photo" role="img" aria-label="Photo of a renovated stone-clad home lit warmly at dusk with garden plants"></div>
    <div class="hero-copy">
      <h1 class="section-title">Welcome to our site</h1>
      <p>Lumo Vant is a Building Design &amp; Drafting studio based in Nedlands Western Australia, providing a high quality and complete client service from concept design through Council planning approvals and building licenses to construction drawings for kitchens and bathrooms, extensions, additions, renovations and new homes.</p>
    </div>
    <div class="slider-dots"><span class="is-active"></span><span></span><span></span><span></span></div>
  </section>

  <section class="services">
    <h2 class="section-title">What we do</h2>
    <div class="carousel-arrows">
      <svg width="10" height="12" viewBox="0 0 10 12" aria-hidden="true"><polygon points="9,1 1,6 9,11" fill="#b8c0c6"/></svg>
      <svg width="10" height="12" viewBox="0 0 10 12" aria-hidden="true"><polygon points="1,1 9,6 1,11" fill="#b8c0c6"/></svg>
    </div>
    <article class="service-card" style="left:90px">
      <div class="service-photo" role="img" aria-label="Photo of a modern kitchen with dark cabinetry and a red tiled splashback" style="background:linear-gradient(135deg,#5a4a48 0%,#7a4b3c 45%,#3a3030 100%)"></div>
      <h3>Kitchens and Bathrooms</h3>
    </article>
    <article class="service-card" style="left:438px">
      <div class="service-photo" role="img" aria-label="Photo of a house extension with a timber deck and outdoor dining at dusk" style="background:linear-gradient(180deg,#2e3f5e 0%,#6e6a55 50%,#4a3a2a 100%)"></div>
      <h3>Extensions</h3>
    </article>
    <article class="service-card" style="left:787px">
      <div class="service-photo" role="img" aria-label="Photo of a stone-clad home addition with garden lighting at night" style="background:linear-gradient(90deg,#1c2a38 0%,#5a4630 55%,#8a6038 100%)"></div>
      <h3>Additions</h3>
    </article>
  </section>

  <footer class="site-footer">
    <ul class="footer-nav">
      <li>Home</li><li>|</li><li>About</li><li>|</li><li>Services</li><li>|</li><li>Projects</li><li>|</li><li>Contact</li>
    </ul>
    <p class="copyright">Copyright © 2013 &nbsp;wwwlumovant.com.au &nbsp; All rights reserved.</p>
    <div class="social" aria-label="Social links"><span></span><span></span></div>
  </footer>
</body>
</html>
```